Business Card Design for Madam Rosette's Soak Parlor

Name: Madam Rosette's Soak Parlor. Maker of bath bombs, bath salts.

Card details:

Dolores Vantick
1.702.555.0193
Las Vegas Nevada
dvantick47@mailbrook.test

"Bath bombs, bath salts and more..."

Industry/Entity Type

Business

Contact Information for Business Card

A picture of an old-fashioned bathtub (with claw feet) filled with bath bombs.

Colors include: Lavender, Pink, Turquois, Light Blue. Can you make the overall design look old fashioned.

```html
<!DOCTYPE html>
<html lang="en">
<head>
<meta charset="utf-8">
<title>Madam Rosette's Soak Parlor – Business Card</title>
<link rel="stylesheet" href="https://fonts.googleapis.com/css2?family=Open+Sans:wght@400;600;700&display=swap">
<style>
  :root {
    --purple: #7b3f9e;
    --teal: #5fc7bf;
    --white: #ffffff;
    --ink: #333333;
    --ink-soft: #555555;
    --backdrop: #e9e7ec;
    --photo-light: #f1f0ee;
    --photo-mid: #c9c8cc;
    --photo-dark: #6f7079;
  }
  * { box-sizing: border-box; margin: 0; padding: 0; }
  html, body {
    width: 1200px; height: 976px; overflow: hidden;
    background: var(--backdrop);
    font-family: "Open Sans", sans-serif;
  }
  .sheet {
    width: 1200px; height: 976px;
    display: flex; flex-direction: column; align-items: center; justify-content: center;
    gap: 40px;
  }
  .card {
    position: relative;
    width: 760px; height: 434px;
    background: var(--white);
    overflow: hidden;
    box-shadow: 0 6px 18px rgba(0,0,0,0.15);
  }

  /* Back side */
  .card-back .photo {
    position: absolute; inset: 0;
    background:
      radial-gradient(ellipse 55% 35% at 50% 48%, var(--photo-dark) 0%, rgba(111,112,121,0.6) 55%, rgba(111,112,121,0) 100%),
      linear-gradient(180deg, var(--photo-light) 0%, var(--photo-mid) 100%);
  }
  .card-back .band {
    position: absolute; left: 110px; top: 414px;
    width: 760px; height: 56px;
    transform-origin: left center;
    transform: rotate(-14deg);
    background: var(--purple);
    display: flex; align-items: center;
    padding-left: 150px;
    color: var(--white); font-weight: 700; font-size: 23px; white-space: nowrap;
  }

  /* Front side */
  .card-front .wave { position: absolute; inset: 0; width: 100%; height: 100%; }
  .contact { position: absolute; left: 78px; top: 140px; }
  .contact .person { font-size: 26px; font-weight: 600; color: var(--ink); margin-bottom: 18px; }
  .contact ul { list-style: none; }
  .contact li {
    display: flex; align-items: center; gap: 14px;
    font-size: 15px; color: var(--ink-soft); margin-bottom: 12px;
  }
  .contact svg { width: 16px; height: 16px; fill: var(--purple); flex: none; }
  .brand { position: absolute; right: 70px; top: 78px; text-align: right; }
  .brand .name {
    font-size: 30px; font-weight: 600; line-height: 1.15; color: var(--purple);
  }
  .brand .maker { font-size: 11px; font-weight: 600; color: var(--ink-soft); margin-top: 8px; }
  .tagline {
    position: absolute; right: 40px; bottom: 40px;
    color: var(--white); font-weight: 700; font-size: 21px;
  }
</style>
</head>
<body>
<main class="sheet">
  <section class="card card-back">
    <div class="photo" role="img" aria-label="Photo of an old-fashioned claw-foot bathtub in a white panelled bathroom"></div>
    <div class="band">Bath bombs, bath salts and more...</div>
  </section>

  <section class="card card-front">
    <svg class="wave" viewBox="0 0 760 434" preserveAspectRatio="none" aria-hidden="true">
      <path d="M0 300 C 200 378, 450 268, 760 222" fill="none" stroke="var(--teal)" stroke-width="10"/>
      <path d="M0 326 C 200 404, 450 294, 760 248 L760 434 L0 434 Z" fill="var(--purple)"/>
    </svg>

    <div class="contact">
      <p class="person">Dolores Vantick</p>
      <ul>
        <li>
          <svg viewBox="0 0 16 16"><path d="M8 1a5 5 0 0 0-5 5c0 3.6 5 9 5 9s5-5.4 5-9a5 5 0 0 0-5-5zm0 7a2 2 0 1 1 0-4 2 2 0 0 1 0 4z"/></svg>
          Las Vegas Nevada
        </li>
        <li>
          <svg viewBox="0 0 16 16"><path d="M3.6 1.5l2.3 2.6-1.3 1.8c.9 2 2.5 3.6 4.5 4.5l1.8-1.3 2.6 2.3-1.2 2.1C7.2 14.9 1.1 8.8 1.5 2.7z"/></svg>
          1.702.555.0193
        </li>
        <li>
          <svg viewBox="0 0 16 16"><path d="M1 3h14v1.2L8 8.5 1 4.2zm0 2.6l7 4.3 7-4.3V13H1z"/></svg>
          dvantick47@mailbrook.test
        </li>
      </ul>
    </div>

    <div class="brand">
      <p class="name">Madam Rosette's<br>Soak Parlor</p>
      <p class="maker">Maker of bath bombs &amp; bath salts</p>
    </div>

    <p class="tagline">Bath bombs, bath salts and more...</p>
  </section>
</main>
</body>
</html>
```